Gentlemen lifestyle blog in need of a logo and webdesign

Velmora is a site all about tests and reviews of products for gentlemen (Gin, whiskey, barber products, outdoor equipment, tobacco, coffe and more). It will be about fashion and a luxury lifestyle, health and fitness.
it will also include a online store

```html
<!DOCTYPE html>
<html lang="en">
<head>
<meta charset="utf-8">
<title>Velmora – Gentleman's Lifestyle Reviews</title>
<link href="https://fonts.googleapis.com/css2?family=Lato:ital,wght@0,400;0,700;0,900;1,400&family=Poppins:wght@800&family=Roboto:wght@700&family=Dancing+Script:wght@700&display=swap" rel="stylesheet">
<style>
:root{
  --blue:#0b4ea2;
  --orange:#ff6a00;
  --ink:#222;
  --muted:#777;
  --line:#e3e3e3;
  --panel:#ececec;
  --white:#fff;
}
*{box-sizing:border-box;margin:0;padding:0}
html,body{width:1200px;height:2605px;overflow:hidden;background:var(--white)}
body{position:relative;font-family:"Lato",sans-serif;color:var(--ink)}
.abs{position:absolute}
.photo{position:absolute;display:block}
/* header */
.logo{left:144px;top:22px;font-family:"Dancing Script",cursive;font-size:44px;color:#111}
.nav{left:390px;top:41px;display:flex;gap:23px;font-size:13.5px;font-weight:700;color:#222}
.nav .active{border-bottom:2px solid var(--orange);padding-bottom:3px}
.cart{left:917px;top:34px;width:30px;height:30px;border-radius:50%;background:var(--orange)}
.login{left:969px;top:29px;width:86px;height:40px;border-radius:20px;background:var(--blue);color:#fff;font-size:13px;display:flex;align-items:center;justify-content:center;gap:7px}
/* hero */
.hero{left:144px;top:103px;width:912px;height:445px;border-radius:20px;overflow:hidden;background:linear-gradient(100deg,#3a2c24 0%,#6a4a30 45%,#b78250 75%,#8a6a58 100%)}
.hero-title{left:229px;top:160px;font-family:"Poppins",sans-serif;font-weight:800;font-size:36px;line-height:45px;color:#fff}
.btn{background:var(--orange);color:#fff;font-weight:700;display:flex;align-items:center;justify-content:center;border-radius:30px}
.hero-btn{left:231px;top:333px;width:170px;height:53px;font-size:15px}
.quote{left:230px;top:432px;font-style:italic;font-size:13.5px;line-height:19px;color:#fff}
.author{left:230px;top:484px;font-size:14px;font-weight:700;color:#fff;display:flex;gap:6px;align-items:center}
.arrow-w{width:36px;height:36px;border-radius:50%;background:#fff}
/* section heads */
.h2{font-family:"Roboto",sans-serif;font-weight:700;font-size:31px;color:var(--blue)}
.tile{position:absolute;width:185px;height:175px;border-radius:14px;overflow:hidden}
.tile span{position:absolute;left:0;right:0;bottom:20px;text-align:center;color:#fff;font-weight:900;font-size:16px;line-height:20px}
.circ-arr{width:28px;height:28px;border:1.5px solid #666;border-radius:50%}
/* cards */
.card{position:absolute;background:#fff;box-shadow:0 2px 8px rgba(0,0,0,.08)}
.card-title{font-size:19px;line-height:22px;color:#333}
.card-text{font-size:12px;line-height:18px;color:var(--muted)}
.meta{font-size:12px;color:#333;display:flex;align-items:center;gap:6px}
.avatar{width:24px;height:24px;border-radius:50%;background:#c9d3e6}
.small-title{font-size:19px;line-height:24px;color:#333}
/* sidebar */
.box{position:absolute;left:785px;width:271px;background:#fff;box-shadow:0 1px 6px rgba(0,0,0,.1)}
.box-head{margin:9px 8px 0;height:44px;background:var(--panel);border:1px solid #ddd;text-align:center;font-family:"Roboto",sans-serif;font-weight:700;font-size:24px;color:var(--blue);line-height:42px}
.field{position:absolute;left:22px;width:221px;height:38px;border:1px solid #eee;font-size:12px;color:#888;padding:13px 18px}
/* footer */
.footer{left:0;top:2333px;width:1200px;height:272px;background:var(--blue);color:#fff}
.ring{width:40px;height:40px;border-radius:50%;border:1.5px solid #fff}
.fnav{display:flex;gap:24px;font-weight:700;font-size:14px}
.soc{width:30px;height:30px;border-radius:50%;border:1.5px solid #fff}
</style>
</head>
<body>

<!-- header -->
<div class="abs logo">Velmora</div>
<nav class="abs nav">
  <span class="active">HOME</span><span>ABOUT</span><span>PRODUCTS</span><span>CATEGORIES</span><span>REVIEWS</span><span>CONTACT US</span>
</nav>
<div class="abs cart"><svg width="30" height="30" viewBox="0 0 30 30"><path d="M8 10h2l2 8h8l2-6H11" fill="none" stroke="#fff" stroke-width="2"/><circle cx="13" cy="21" r="1.4" fill="#fff"/><circle cx="19" cy="21" r="1.4" fill="#fff"/></svg></div>
<div class="abs login"><svg width="12" height="12" viewBox="0 0 12 12"><circle cx="6" cy="3.5" r="3" fill="#fff"/><path d="M0 12c0-4 3-5 6-5s6 1 6 5z" fill="#fff"/></svg>LOGIN</div>

<!-- hero -->
<div class="abs hero" role="img" aria-label="Traveller with backpack raising his arms on a beach at sunset"></div>
<h1 class="abs hero-title">Refining the<br>Gentleman’s Lifestyle<br>One Review at a Time.</h1>
<div class="abs btn hero-btn">GET STARTED</div>
<p class="abs quote">“Sed ut perspiciatis unde omnis iste natus error sit voluptatem<br>accusantium doloremque litectaea sunt explicabo”</p>
<div class="abs author">-ALEX MARSH, <svg width="80" height="15" viewBox="0 0 80 15"><g fill="#ffb400"><path id="st" d="M7.5 0l2.2 4.7 5.1.6-3.8 3.5 1 5.1-4.5-2.6-4.5 2.6 1-5.1L.2 5.3l5.1-.6z"/><use href="#st" x="16"/><use href="#st" x="32"/><use href="#st" x="48"/><use href="#st" x="64"/></g></svg></div>
<div class="abs arrow-w" style="left:942px;top:462px"><svg width="36" height="36"><path d="M20 11l-7 7 7 7" fill="none" stroke="#111" stroke-width="2"/></svg></div>
<div class="abs arrow-w" style="left:986px;top:462px"><svg width="36" height="36"><path d="M16 11l7 7-7 7" fill="none" stroke="#111" stroke-width="2"/></svg></div>

<!-- featured categories -->
<h2 class="abs h2" style="left:143px;top:610px">FEATURED CATEGORIES</h2>
<div class="tile" style="left:145px;top:668px;background:linear-gradient(#6a6a5e,#2a2a26)" role="img" aria-label="Bartender garnishing a gin cocktail"><span>GIN</span></div>
<div class="tile" style="left:341px;top:668px;background:linear-gradient(#7a4a26,#2a1c14)" role="img" aria-label="Whiskey being poured into a glass"><span>WHISKEY</span></div>
<div class="tile" style="left:537px;top:668px;background:linear-gradient(#5a5a5a,#1e1e1e)" role="img" aria-label="Barber tools and clippers"><span>BARBER<br>PRODUCTS</span></div>
<div class="tile" style="left:145px;top:855px;background:linear-gradient(#c87a48,#3a3430)" role="img" aria-label="Camping tent and outdoor gear"><span>OUTDOOR<br>EQUIPMENT</span></div>
<div class="tile" style="left:341px;top:855px;background:linear-gradient(#8a5a2e,#3a2414)" role="img" aria-label="Loose tobacco leaves and cigarette"><span>TOBACCO</span></div>
<div class="tile" style="left:537px;top:855px;background:linear-gradient(#6a4a34,#2a1e18)" role="img" aria-label="Coffee beans around a cup"><span>COFFEE</span></div>
<div class="tile" style="left:145px;top:1042px;background:linear-gradient(#9a958e,#3a3632)" role="img" aria-label="Man in winter fashion outfit"><span>FASHION</span></div>
<div class="tile" style="left:341px;top:1042px;background:linear-gradient(#c08a52,#3a2e28)" role="img" aria-label="Couple on a terrace at sunset"><span>LUXURY LIFESTYLE</span></div>
<div class="tile" style="left:537px;top:1042px;background:linear-gradient(#7a7266,#2a2824)" role="img" aria-label="Fitness tracker and phone with charts"><span>HEALTH AND<br>FITNESS</span></div>

<!-- recent blogs -->
<h2 class="abs h2" style="left:143px;top:1270px">RECENT BLOGS</h2>
<div class="abs circ-arr" style="left:676px;top:1274px"><svg width="25" height="25"><path d="M18 12.5H7m4-4-4 4 4 4" fill="none" stroke="#555" stroke-width="1.5"/></svg></div>
<div class="abs circ-arr" style="left:709px;top:1274px"><svg width="25" height="25"><path d="M7 12.5h11m-4-4 4 4-4 4" fill="none" stroke="#555" stroke-width="1.5"/></svg></div>

<div class="card" style="left:144px;top:1335px;width:274px;height:355px">
  <div class="photo" style="left:0;top:0;width:274px;height:175px;background:linear-gradient(#6a4a30,#a0402a)" role="img" aria-label="Friends toasting with wine glasses"></div>
  <div class="abs avatar" style="left:24px;top:202px"></div>
  <div class="abs card-title" style="left:63px;top:198px">Lorem ipsum dolor sit<br>amet conseactetur</div>
  <p class="abs card-text" style="left:24px;top:256px">Sed ut perspiciatis unde omnis iste natus<br>error sit voluptatem accusantium</p>
  <div class="abs" style="left:24px;top:302px;width:232px;border-top:1px solid var(--line)"></div>
  <div class="abs meta" style="left:24px;top:319px"><svg width="11" height="11"><rect x=".5" y="1.5" width="10" height="9" fill="none" stroke="#ff6a00"/></svg>March 23,2025 &nbsp;| &nbsp;<svg width="12" height="10"><ellipse cx="6" cy="4.5" rx="6" ry="4.5" fill="#ff6a00"/></svg>32</div>
</div>

<div class="photo" style="left:444px;top:1335px;width:121px;height:95px;background:linear-gradient(#c0a896,#5a4a42)" role="img" aria-label="Hairdresser styling hair"></div>
<div class="abs small-title" style="left:581px;top:1343px">Lorem ipsum dolor<br>sit amet</div>
<div class="abs meta" style="left:581px;top:1404px"><svg width="11" height="11"><rect x=".5" y="1.5" width="10" height="9" fill="none" stroke="#ff6a00"/></svg>March 23,2025 &nbsp;&nbsp;| &nbsp;&nbsp;<svg width="12" height="10"><ellipse cx="6" cy="4.5" rx="6" ry="4.5" fill="#ff6a00"/></svg>32</div>
<div class="photo" style="left:444px;top:1443px;width:121px;height:95px;background:linear-gradient(#3a3430,#b07a3a)" role="img" aria-label="Whiskey glasses at a party"></div>
<div class="abs small-title" style="left:581px;top:1451px">Lorem ipsum dolor<br>sit amet</div>
<div class="abs meta" style="left:581px;top:1512px"><svg width="11" height="11"><rect x=".5" y="1.5" width="10" height="9" fill="none" stroke="#ff6a00"/></svg>March 23,2025 &nbsp;&nbsp;| &nbsp;&nbsp;<svg width="12" height="10"><ellipse cx="6" cy="4.5" rx="6" ry="4.5" fill="#ff6a00"/></svg>32</div>
<div class="photo" style="left:444px;top:1551px;width:121px;height:95px;background:linear-gradient(#9aa0a8,#3a4a6a)" role="img" aria-label="Woman in denim jacket using a phone in the city"></div>
<div class="abs small-title" style="left:581px;top:1559px">Lorem ipsum dolor<br>sit amet</div>
<div class="abs meta" style="left:581px;top:1620px"><svg width="11" height="11"><rect x=".5" y="1.5" width="10" height="9" fill="none" stroke="#ff6a00"/></svg>March 23,2025 &nbsp;&nbsp;| &nbsp;&nbsp;<svg width="12" height="10"><ellipse cx="6" cy="4.5" rx="6" ry="4.5" fill="#ff6a00"/></svg>32</div>
<div class="abs" style="left:444px;top:1674px;color:var(--orange);font-size:16px;font-weight:700">VIEW MORE</div>

<!-- share bar -->
<div class="abs" style="left:144px;top:1734px;width:614px;height:52px;border-top:1px solid var(--line);border-bottom:1px solid var(--line)"></div>
<div class="abs" style="left:165px;top:1751px;font-size:17px;font-weight:700;color:#333">SHARE ON</div>
<div class="abs" style="left:273px;top:1747px;width:27px;height:27px;border-radius:50%;background:#2b58a8"></div>
<div class="abs" style="left:305px;top:1747px;width:27px;height:27px;border-radius:50%;background:#1a8ee0"></div>
<div class="abs" style="left:337px;top:1747px;width:27px;height:27px;border-radius:50%;background:#7a6a5e"></div>
<div class="abs btn" style="left:590px;top:1741px;width:143px;height:38px;font-size:15px;gap:6px">COMMENT <svg width="12" height="12"><circle cx="6" cy="6" r="6" fill="#fff"/><path d="M5 3l3 3-3 3" fill="none" stroke="#ff6a00" stroke-width="1.6"/></svg></div>

<!-- popular posts -->
<h2 class="abs h2" style="left:143px;top:1835px">POPULAR POSTS</h2>
<div class="abs circ-arr" style="left:676px;top:1839px"><svg width="25" height="25"><path d="M18 12.5H7m4-4-4 4 4 4" fill="none" stroke="#555" stroke-width="1.5"/></svg></div>
<div class="abs circ-arr" style="left:709px;top:1839px"><svg width="25" height="25"><path d="M7 12.5h11m-4-4 4 4-4 4" fill="none" stroke="#555" stroke-width="1.5"/></svg></div>

<div class="card" style="left:144px;top:1900px;width:283px;height:355px">
  <div class="photo" style="left:0;top:0;width:283px;height:175px;background:linear-gradient(#e6c68a,#8a6a30)" role="img" aria-label="Family running through a golden field"></div>
  <div class="abs avatar" style="left:24px;top:202px"></div>
  <div class="abs card-title" style="left:63px;top:198px">Lorem ipsum dolor sit<br>amet conseactetur</div>
  <p class="abs card-text" style="left:24px;top:256px">Sed ut perspiciatis unde omnis iste natus<br>error sit voluptatem accusantium</p>
  <div class="abs" style="left:24px;top:302px;width:236px;border-top:1px solid var(--line)"></div>
  <div class="abs meta" style="left:24px;top:319px"><svg width="11" height="11"><rect x=".5" y="1.5" width="10" height="9" fill="none" stroke="#ff6a00"/></svg>March 23,2025 &nbsp;| &nbsp;<svg width="12" height="10"><ellipse cx="6" cy="4.5" rx="6" ry="4.5" fill="#ff6a00"/></svg>32</div>
</div>
<div class="card" style="left:455px;top:1900px;width:283px;height:355px">
  <div class="photo" style="left:0;top:0;width:283px;height:175px;background:linear-gradient(90deg,#2e4450,#6a5446,#a08466)" role="img" aria-label="Woman drinking coffee by a window"></div>
  <div class="abs avatar" style="left:34px;top:202px"></div>
  <div class="abs card-title" style="left:71px;top:198px">Lorem ipsum dolor sit<br>amet conseactetur</div>
  <p class="abs card-text" style="left:32px;top:256px">Sed ut perspiciatis unde omnis iste natus<br>error sit voluptatem accusantium</p>
  <div class="abs" style="left:32px;top:302px;width:236px;border-top:1px solid var(--line)"></div>
  <div class="abs meta" style="left:32px;top:319px"><svg width="11" height="11"><rect x=".5" y="1.5" width="10" height="9" fill="none" stroke="#ff6a00"/></svg>March 23,2025 &nbsp;| &nbsp;<svg width="12" height="10"><ellipse cx="6" cy="4.5" rx="6" ry="4.5" fill="#ff6a00"/></svg>32</div>
</div>

<!-- sidebar: search -->
<div class="box" style="top:608px;height:130px">
  <div class="box-head">SEARCH</div>
  <div class="abs" style="left:20px;top:67px;width:231px;height:40px;border:1px solid #ddd;border-radius:20px;font-size:12px;color:#666;padding:13px 20px">Search..</div>
  <div class="abs" style="left:217px;top:74px;width:27px;height:27px;border-radius:50%;background:var(--orange)"><svg width="27" height="27"><circle cx="12.5" cy="12.5" r="4.5" fill="none" stroke="#fff" stroke-width="2"/><path d="M16 16l3.5 3.5" stroke="#fff" stroke-width="2"/></svg></div>
</div>

<!-- sidebar: about -->
<div class="box" style="top:760px;height:357px;overflow:hidden">
  <div class="box-head">ABOUT</div>
  <div class="photo" style="left:0;top:220px;width:271px;height:137px;background:linear-gradient(#fff 0%,#7aa6b8 35%,#2e6a80 100%)" role="img" aria-label="Kayaker paddling among sea cliffs"></div>
  <p class="abs" style="left:18px;top:78px;width:235px;text-align:center;font-size:14px;line-height:21px;color:#666">Sed ut perspiciatis unde omnis iste natus error sit voluptatem cusantium doloremque laudantium, totam rem aperiam, eaque ipsa quae ab illo invened ut perspiciatis unde omnis iste natus error sit voluptatem</p>
  <div class="abs btn" style="left:69px;top:223px;width:134px;height:41px;font-size:15px">READ MORE</div>
</div>

<!-- sidebar: newsletter -->
<div class="box" style="top:1140px;height:253px">
  <div class="box-head">NEWSLETTER</div>
  <p class="abs" style="left:0;width:271px;top:66px;text-align:center;font-size:14px;color:#333">Lorem ipsum dolo sit amet</p>
  <div class="field" style="top:97px">Enter Name</div>
  <div class="field" style="top:148px">Enter Email</div>
  <div class="abs btn" style="left:24px;top:198px;width:223px;height:39px;font-size:15px">SIGN UP</div>
</div>

<!-- sidebar: follow -->
<div class="box" style="top:1418px;height:250px">
  <div class="box-head">FOLLOW US</div>
  <div class="photo" style="left:21px;top:76px;width:71px;height:61px;background:linear-gradient(#cfcac2,#7a6a5e)" role="img" aria-label="Lifestyle photo"></div>
  <div class="photo" style="left:101px;top:76px;width:71px;height:61px;background:linear-gradient(#d6b49a,#8a5a40)" role="img" aria-label="Lifestyle photo"></div>
  <div class="photo" style="left:181px;top:76px;width:71px;height:61px;background:linear-gradient(#c6c2bc,#5a5450)" role="img" aria-label="Lifestyle photo"></div>
  <div class="photo" style="left:21px;top:146px;width:71px;height:61px;background:linear-gradient(#c8a890,#7a5a48)" role="img" aria-label="Lifestyle photo"></div>
  <div class="photo" style="left:101px;top:146px;width:71px;height:61px;background:linear-gradient(#b8bcc0,#5a6066)" role="img" aria-label="Lifestyle photo"></div>
  <div class="photo" style="left:181px;top:146px;width:71px;height:61px;background:linear-gradient(#d8c0a4,#8a6a52)" role="img" aria-label="Lifestyle photo"></div>
  <div class="abs" style="left:0;width:271px;top:224px;text-align:center;font-size:13px;color:var(--orange);text-decoration:underline">Follow us on our photo feed</div>
</div>

<!-- sidebar: videos -->
<div class="box" style="top:1694px;height:561px">
  <div class="box-head">VIDEOS</div>
  <div class="photo" style="left:21px;top:76px;width:231px;height:125px;background:linear-gradient(#e6e2dc,#a06a30)" role="img" aria-label="Video: rows of cigarettes"></div>
  <div class="photo" style="left:21px;top:210px;width:231px;height:125px;background:linear-gradient(#a8b8c8,#6a5e54)" role="img" aria-label="Video: woman overlooking a city skyline"></div>
  <div class="photo" style="left:21px;top:344px;width:231px;height:125px;background:linear-gradient(#4a4440,#1e1c1a)" role="img" aria-label="Video: woman training at the gym"></div>
  <svg class="abs" style="left:122px;top:124px" width="30" height="30"><circle cx="15" cy="15" r="15" fill="#e53935"/><path d="M12 9l9 6-9 6z" fill="#fff"/></svg>
  <svg class="abs" style="left:122px;top:258px" width="30" height="30"><circle cx="15" cy="15" r="15" fill="#e53935"/><path d="M12 9l9 6-9 6z" fill="#fff"/></svg>
  <svg class="abs" style="left:122px;top:392px" width="30" height="30"><circle cx="15" cy="15" r="15" fill="#e53935"/><path d="M12 9l9 6-9 6z" fill="#fff"/></svg>
  <div class="abs btn" style="left:76px;top:500px;width:120px;height:41px;font-size:11px;gap:4px">VIEW MORE <svg width="10" height="10"><circle cx="5" cy="5" r="5" fill="#fff"/><path d="M4 2.5l2.5 2.5L4 7.5" fill="none" stroke="#ff6a00" stroke-width="1.4"/></svg></div>
</div>

<!-- footer -->
<footer class="abs footer">
  <div class="abs ring" style="left:237px;top:70px"><svg width="37" height="37"><path d="M18.5 10a5 5 0 0 1 5 5c0 4-5 10-5 10s-5-6-5-10a5 5 0 0 1 5-5z" fill="#fff"/><circle cx="18.5" cy="15" r="1.8" fill="#0b4ea2"/></svg></div>
  <div class="abs" style="left:294px;top:73px;font-size:13.5px;line-height:22px">314,At vero eos et accu<br>samus et iusto odio dimos ducimu</div>
  <div class="abs" style="left:545px;top:70px;width:40px;height:40px;border-radius:50%;background:var(--orange)"><svg width="40" height="40"><path d="M14 13c1-1 2-1 3 0l2 3-2 2c1 2 3 4 5 5l2-2 3 2c1 1 1 2 0 3-2 2-5 1-9-3s-6-8-4-10z" fill="#fff"/></svg></div>
  <div class="abs" style="left:598px;top:81px;font-size:15px;font-weight:700">+ 1 555 010 2040</div>
  <div class="abs ring" style="left:758px;top:70px"><svg width="37" height="37"><rect x="10" y="12" width="17" height="13" rx="1.5" fill="#fff"/><path d="M10 13l8.5 6 8.5-6" fill="none" stroke="#0b4ea2" stroke-width="1.4"/></svg></div>
  <div class="abs" style="left:814px;top:81px;font-size:14px">hello@velmora-mail.com</div>
  <nav class="abs fnav" style="left:348px;top:130px"><span>HOME</span><span>ABOUT</span><span>PRODUCTS</span><span>CATEGORIES</span><span>REVIEWS</span><span>CONTACT US</span></nav>
  <div class="abs" style="left:0;top:167px;width:1200px;border-top:1px solid rgba(255,255,255,.2)"></div>
  <div class="abs" style="left:144px;top:203px;font-size:14px">Copyrights © 2025, Velmora.All rights reserved &nbsp;| &nbsp;Privacy Policy &nbsp;| &nbsp;Terms of Use</div>
  <div class="abs soc" style="left:917px;top:197px"></div>
  <div class="abs soc" style="left:953px;top:197px;background:var(--orange);border-color:var(--orange)"></div>
  <div class="abs soc" style="left:989px;top:197px"></div>
  <div class="abs soc" style="left:1025px;top:197px"></div>
</footer>

</body>
</html>
```